Online Rug Store needs Clearance Banner

Website is: Marvelous Mats and Interiors
You can access it at: www.marvelousmatsandinteriors-example.com and login (top right) with password: plorvat

*** update: When creating banners for my site, you have permission to use images from www.kelvora-example.com, but ONLY for this project. The images/artwork are copyright allowable for use on www.marvelousmatsandinteriors-example.com projects.***

We need a home page banner sized 1000 wide x 500 tall pixels to promote a "Clearance Sale" on rugs. The banner can state:

1. Clearance Sale
2. Now in progress
3. Save an extra 20% with coupon code 'Take20'
4. Ends March 31st
5. Plus Free Shipping and 30 day returns.

We prefer a banner that appears hand-drawn and artistic, not commercially produced. It is OK to use a room scene image, rug images, or just a colored/textured background with text and no images. Your choice.

Flat graphics with no shadows and 3-D effect preferred.
Attached is are 3 logo options, as well as an example banner with handcrafted, artistic styling that we prefer.

Target Market(s)

This should be an eye-catching banner to showcase a very urgent promotion. Consider using colors of red, white, gold, and black to make a strong statement on the home page.

Industry/Entity Type

Home And Garden

Requirements
Must have
• Winner must provide Photoshop editable file format (.psd format) including layers that can be edited.
Nice to have
• Hand-drawn, stenciled, scribbled, artistic graphics and fonts is nice because we sell rugs that are made by hand.
Should not have
• little to no shadowing. Avoid computerized graphics.

```html
<!DOCTYPE html>
<html lang="en">
<head>
<meta charset="UTF-8">
<title>Clearance Sale Banner</title>
<link rel="stylesheet" href="https://fonts.googleapis.com/css2?family=Amatic+SC:wght@700&family=Kaushan+Script&family=Montserrat:wght@500&family=Varela+Round&display=swap">
<style>
  :root {
    --backdrop: #86806f;
    --sale-red: #760000;
    --pattern-red: #9a1a1a;
    --pattern-gold: #8a6a1c;
    --pattern-dark: #3b1410;
    --ink-white: #ffffff;
    --accent-gold: #e0b02a;
  }
  * { margin: 0; padding: 0; box-sizing: border-box; }
  html, body {
    width: 1200px;
    height: 1200px;
    overflow: hidden;
    background: var(--backdrop);
  }
  .canvas {
    position: relative;
    width: 1200px;
    height: 1200px;
  }
  .banner {
    position: absolute;
    left: 100px;
    top: 350px;
    width: 1000px;
    height: 500px;
  }
  .banner__pattern {
    position: absolute;
    inset: 0;
    background: linear-gradient(135deg, var(--pattern-red) 0%, var(--pattern-gold) 50%, var(--pattern-dark) 100%);
  }
  .banner__panel {
    position: absolute;
    left: 84px;
    top: 84px;
    width: 842px;
    height: 336px;
    background: var(--sale-red);
    outline: 1px solid rgba(255,255,255,0.7);
    color: var(--ink-white);
  }
  .headline {
    position: absolute;
    left: 0;
    right: 0;
    top: 14px;
    text-align: center;
    white-space: nowrap;
    padding-left: 40px;
  }
  .headline__caps {
    font-family: "Amatic SC", sans-serif;
    font-weight: 700;
    font-size: 96px;
    letter-spacing: 8px;
    vertical-align: baseline;
  }
  .headline__script {
    font-family: "Kaushan Script", cursive;
    font-size: 100px;
    margin-left: 10px;
    vertical-align: baseline;
  }
  .subhead {
    position: absolute;
    left: 0;
    right: 0;
    top: 118px;
    text-align: center;
    white-space: nowrap;
  }
  .subhead__script {
    font-family: "Kaushan Script", cursive;
    font-size: 46px;
    margin-right: 18px;
  }
  .subhead__caps {
    font-family: "Amatic SC", sans-serif;
    font-weight: 700;
    font-size: 52px;
    letter-spacing: 5px;
  }
  .offer {
    position: absolute;
    left: 0;
    right: 0;
    top: 196px;
    text-align: center;
    white-space: nowrap;
    padding-left: 30px;
  }
  .offer__text {
    font-family: "Montserrat", sans-serif;
    font-weight: 500;
    font-size: 19px;
    letter-spacing: 3px;
  }
  .offer__accent {
    font-family: "Kaushan Script", cursive;
    font-size: 30px;
    color: var(--accent-gold);
    margin: 0 6px;
  }
  .offer__code {
    font-family: "Amatic SC", sans-serif;
    font-weight: 700;
    font-size: 40px;
    letter-spacing: 3px;
    color: var(--accent-gold);
    margin-left: 6px;
  }
  .footnote {
    position: absolute;
    bottom: 12px;
    font-family: "Varela Round", sans-serif;
    font-size: 24px;
  }
  .footnote--left { left: 14px; }
  .footnote--right { right: 16px; bottom: 10px; }
</style>
</head>
<body>
  <main class="canvas">
    <section class="banner">
      <div class="banner__pattern" role="img" aria-label="Rug-inspired diamond tile pattern border in red, gold, black and white"></div>
      <div class="banner__panel">
        <h1 class="headline">
          <span class="headline__caps">CLEARANCE</span><span class="headline__script">Sale</span>
        </h1>
        <p class="subhead">
          <span class="subhead__script">Now</span><span class="subhead__caps">IN PROGRESS</span>
        </p>
        <p class="offer">
          <span class="offer__text">Save an</span><span class="offer__accent">extra 20%</span><span class="offer__text">with coupon code</span><span class="offer__code">'TAKE20'</span>
        </p>
        <p class="footnote footnote--left">Plus Free Shipping and 30 day returns</p>
        <p class="footnote footnote--right">Ends March 31st</p>
      </div>
    </section>
  </main>
</body>
</html>
```